Brochure Design Project

We need a brochure to introduce clients who work in our local area to become a VIP clients based on the fact they work in the local area. We have call centers of major companies with 1 km of our hair salon as well as head offices of many big companies some with staff of 400 and Australia second biggest University Carrowby with 1500 international student who live mins away who use our local shops to have lunch as we have many food outlets we have a wide mix of people walking past our salon at lunch time demographic ages from 19yo call center staff to CEO's. I not sure whether to use VIP what are your thoughts and statistics say (overuse). I need your thoughts on how they would qualify to become a VIP i was thinking they only need to show proof they work in one of the offices in our area to become a member I will provide them with a small plastic bar coded tag to identify themselves if they become members you can profile our business from our website www.vessoria.com.au our NEW logo is on our facebook page Vessoria Hair and Make up web logo is the old one I think we should put in our price list which is on our website i was thinking 20% off normal prices subject to change.

Reason: I need more time to organize staff

Target Market(s)

Local traders and local offices we have many call centre staff and big company head offices with in 1 km

Industry/Entity Type

Plastic

Requirements
Must have
• Simplicity not too busy less is more
Nice to have
• A4 Folded
Should not have
• Too much text

```html
<!DOCTYPE html>
<html lang="en">
<head>
<meta charset="utf-8">
<title>Vessoria Hair and Make up — Price List</title>
<link href="https://fonts.googleapis.com/css2?family=Cormorant+Garamond:wght@400;500&display=swap" rel="stylesheet">
<style>
  :root {
    --paper: #ffffff;
    --ink: #0a0a0a;
    --light: #f2f2f2;
    --orange: #f47b20;
    --photo-top: #dcdcdc;
    --photo-bottom: #8a8a8a;
  }
  * { margin: 0; padding: 0; box-sizing: border-box; }
  html, body { width: 1200px; height: 1000px; overflow: hidden; background: var(--paper); }
  body { font-family: "Cormorant Garamond", "Times New Roman", serif; font-weight: 500; color: var(--light); }
  .spread { position: relative; width: 1200px; height: 1000px; }

  .about-panel { position: absolute; left: 0; top: 76px; width: 404px; height: 847px; overflow: hidden; }
  .about-photo { position: absolute; inset: 0;
    background:
      linear-gradient(180deg, transparent 0 56%, rgba(244,123,32,.85) 56% 63%, transparent 63%),
      linear-gradient(180deg, var(--photo-top), var(--photo-bottom)); }
  .about-title { position: absolute; left: 268px; top: 44px; font-size: 21px; font-weight: 400;
    letter-spacing: .02em; border-bottom: 1.5px solid var(--light); padding-bottom: 2px; color: #fff; }
  .about-box { position: absolute; left: 37px; top: 484px; width: 354px; height: 313px;
    background: var(--orange); color: #fff; padding: 8px 8px 0 11px; font-size: 15px; line-height: 19px; }
  .about-box p + p { margin-top: 18px; }

  .price-panel { position: absolute; left: 404px; top: 76px; width: 796px; height: 847px; background: var(--ink); }
  .title-hair { position: absolute; left: 208px; top: 42px; font-size: 22px; font-weight: 400;
    border-bottom: 1.5px solid var(--light); padding-bottom: 3px; letter-spacing: .02em; }
  .price-list-title { position: absolute; left: 54px; top: 183px; font-size: 21px; font-weight: 400; }
  .text { position: absolute; font-size: 15px; line-height: 19.5px; }
  .row { position: absolute; font-size: 15px; line-height: 19px; white-space: nowrap; }
  .row span { position: absolute; top: 0; }
  .head { text-transform: uppercase; letter-spacing: .02em; }
  .col-b .c1 { left: 182px; width: 100px; text-align: center; }
  .col-b .c2 { left: 286px; width: 100px; text-align: center; }
  .col-c .c1 { left: 553px; width: 100px; text-align: center; }
  .col-c .c2 { left: 656px; width: 100px; text-align: center; }
  .col-b .lbl { left: 54px; }
  .col-c .lbl { left: 442px; }
  .stack { line-height: 19px; }
</style>
</head>
<body>
<div class="spread">

  <section class="about-panel">
    <div class="about-photo" role="img" aria-label="Black and white fashion photograph of a model with long straight hair and a fringe, over bold orange brush strokes"></div>
    <h2 class="about-title">ABOUT US</h2>
    <div class="about-box">
      <p>After nearly three decades, Vessoria is somewhat of an institution in hairdressing in Melbourne.</p>
      <p>Tradition, prestige and innovation set the foundations for what the salon epitomises. It embodies a culture where technique meets creativity to produce work of the highest calibre.</p>
      <p>An infusion of both modernity and opulence are the cornerstone in manifesting our lifestyle salons of style and sophistication.</p>
      <p>Vessoria is no stranger to the media spotlight. With over 70 awards and accolades, both nationally and internationally, it has earned an enviable reputation for hair excellence and service quality.</p>
    </div>
  </section>

  <section class="price-panel">
    <h2 class="title-hair">ALL THINGS HAIR</h2>
    <p class="text" style="left:54px;top:106px;width:345px;">Orvane Professionnel and Velanza Paris are the salon’s premium products of choice. A strong partnership Vessoria has shared for many years.</p>
    <h3 class="price-list-title">PRICE LIST</h3>

    <div class="col-b">
      <div class="row head" style="top:222px;"><span class="lbl">Cutting</span><span class="c1 stack">STYLE<br>DIRECTOR</span><span class="c2 stack">PRINCIPAL<br>STYLIST</span></div>
      <div class="row" style="top:268px;"><span class="lbl">Ladies’ Style Cut *</span><span class="c1">$80.00</span><span class="c2">$70.00</span></div>
      <div class="row" style="top:287px;"><span class="lbl">Mens’ Style Cut *</span><span class="c1">$55.00</span><span class="c2">$45.00</span></div>
      <p class="text" style="left:54px;top:314px;width:340px;">*Salon Director – from $90.00 (Ladies) and from $65.00 (Men)</p>
      <div class="row head" style="top:366px;"><span class="lbl stack" style="line-height:15px;">Blow wave/<br>Styling</span></div>
      <div class="row" style="top:427px;"><span class="lbl">Short</span><span class="c1">$50.00</span><span class="c2">$40.00</span></div>
      <div class="row" style="top:447px;"><span class="lbl">Medium</span><span class="c1">$60.00</span><span class="c2">$50.00</span></div>
      <div class="row" style="top:468px;"><span class="lbl">Long</span><span class="c1">$70.00</span><span class="c2">$60.00</span></div>
      <div class="row head" style="top:502px;"><span class="lbl">Colours</span></div>
      <p class="text" style="left:54px;top:550px;width:345px;">Colour consultations explore a client’s eye colour, skin tone, wants, needs and lifestyle . We offer directional advice, believing it is paramount in stimulating creativity for new ideas or for the refreshment of existing colour.</p>
      <div class="row head" style="top:665px;"><span class="lbl">Colouring</span><span class="c1 stack">TECHNICAL<br>DIRECTOR</span><span class="c2 stack">PRINCIPAL<br>COLOURIST</span></div>
      <div class="row" style="top:715px;"><span class="lbl">Regrowth</span><span class="c1">$80.00</span><span class="c2">$65.00</span></div>
      <div class="row" style="top:736px;"><span class="lbl">Short</span><span class="c1">$80.00</span><span class="c2">$70.00</span></div>
      <div class="row" style="top:757px;"><span class="lbl">Medium</span><span class="c1">$90.00</span><span class="c2">$80.00</span></div>
      <div class="row" style="top:779px;"><span class="lbl">Long</span><span class="c1">$100.00</span><span class="c2">$90.00</span></div>
    </div>

    <div class="col-c">
      <div class="row head" style="top:45px;"><span class="lbl stack">NOVA<br>(AMMONIA<br>&nbsp;FREE)</span><span class="c1 stack">TECHNICAL<br>DIRECTOR</span><span class="c2 stack">PRINCIPAL<br>COLOURIST</span></div>
      <div class="row" style="top:127px;"><span class="lbl">Regrowth</span><span class="c1">$85.00</span><span class="c2">$75.00</span></div>
      <div class="row" style="top:149px;"><span class="lbl">Short</span><span class="c1">$90.00</span><span class="c2">$80.00</span></div>
      <div class="row" style="top:171px;"><span class="lbl">Medium</span><span class="c1">$100.00</span><span class="c2">$95.00</span></div>
      <div class="row" style="top:192px;"><span class="lbl">Long</span><span class="c1">$110.00</span><span class="c2">$110.00</span></div>
      <div class="row head" style="top:235px;"><span class="lbl">Foiling</span></div>
      <div class="row" style="top:280px;"><span class="lbl">1/2 &nbsp;&nbsp;Head</span><span class="c1">$110.00</span><span class="c2">$85.00</span></div>
      <div class="row" style="top:302px;"><span class="lbl">Full Head</span><span class="c1">$170.00</span><span class="c2">$145.00</span></div>
      <div class="row" style="top:321px;"><span class="lbl">Toner</span><span class="c1">$15.00</span><span class="c2">$10.00</span></div>
      <div class="row head" style="top:348px;"><span class="lbl stack">Foils and<br>Colour</span></div>
      <div class="row" style="top:411px;"><span class="lbl">Short</span><span class="c1">$125.00</span><span class="c2">$125.00</span></div>
      <div class="row" style="top:431px;"><span class="lbl">Medium</span><span class="c1">$135.00</span><span class="c2">$130.00</span></div>
      <div class="row" style="top:452px;"><span class="lbl">Long</span><span class="c1">$145.00</span><span class="c2">$140.00</span></div>
      <div class="row" style="top:473px;"><span class="lbl">Toner</span><span class="c1">$15.00</span><span class="c2">$10.00</span></div>
      <div class="row head" style="top:515px;"><span class="lbl stack">NOVA<br>(AMMONIA FREE)</span></div>
      <div class="row" style="top:583px;"><span class="lbl">Medium</span><span class="c1">$160.00</span><span class="c2">$145.00</span></div>
      <div class="row" style="top:603px;"><span class="lbl">Long</span><span class="c1">$170.00</span><span class="c2">$160.00</span></div>
      <div class="row" style="top:626px;"><span class="lbl">Toner</span><span class="c1">$15.00</span><span class="c2">$10.00</span></div>
      <div class="row head" style="top:670px;"><span class="lbl">Bridal hair/formal hair</span></div>
      <div class="row" style="top:715px;"><span class="lbl">Please contact salon for details.</span></div>
      <div class="row" style="top:734px;"><span class="lbl" style="letter-spacing:.06em;">Phone: 9123 4570</span></div>
    </div>
  </section>

</div>
</body>
</html>
```